7 ¾ long by 5 inches high print ad

I have a 1/2 page ad for a print magazine I need to be designed. Uploaded is the previous year design. We want something to be more aligned with our new website look/feel and new messaging from website.

I have provided some photos, the logo, color codes and a recent banner ad sample for copy.

Target Market(s)

Developers

Font styles to use
Sans Serif

Requirements
Must have
• Clear headline, sub headline, and value statement
• Services to highlight, Tilt-Up Construction,
• Website, phone, social icons, Facebook, Twitter, and LinkedIn
Nice to have
• https://marrowcrestbuilding.com/
• Some of the logos in the clients who trust us section

```html
<!DOCTYPE html>
<html lang="en">
<head>
<meta charset="utf-8">
<title>Marrowcrest Construction – Print Ad</title>
<link href="https://fonts.googleapis.com/css2?family=Archivo:wght@400;700;800&family=Arimo:wght@400;700&family=Roboto+Condensed:wght@300;700&display=swap" rel="stylesheet">
<style>
:root{
  --stage:#48494e;
  --white:#ffffff;
  --orange:#cc7c00;
  --orange-light:#e0a040;
  --navy:#2b3562;
  --slate:#585a60;
  --ink:#45464b;
  --dark:#1f2440;
}
*{margin:0;padding:0;box-sizing:border-box}
html,body{width:1200px;height:969px;overflow:hidden;background:var(--stage)}
body{font-family:"Arimo",Arial,sans-serif;position:relative}
.ad{position:absolute;left:172px;top:179px;width:857px;height:612px;background:var(--white);overflow:hidden}
.header{position:absolute;left:0;top:0;width:857px;height:121px}
.headline{position:absolute;left:42px;top:50px;font-family:"Archivo",sans-serif;font-weight:800;font-size:24px;line-height:29px;color:var(--ink)}
.brand{position:absolute;left:539px;top:33px;display:flex;align-items:center;gap:10px}
.brand-mark{width:43px;height:69px;background:var(--orange)}
.brand-name{font-family:"Arimo",sans-serif;color:var(--orange);line-height:1}
.brand-name .n1{display:block;font-size:33px;font-weight:400}
.brand-name .n2{display:block;font-size:18px;font-weight:400;margin-left:4px;margin-top:2px}
.cell{position:absolute;width:286px;height:205px;overflow:hidden}
.photo-store{left:0;top:121px;background:linear-gradient(180deg,#c9d5e2 0%,#b9a894 55%,#7b6e63 100%)}
.years{left:286px;top:121px;width:285px;background:var(--orange);color:var(--white);text-align:center}
.photo-lot{left:571px;top:121px;background:linear-gradient(180deg,#b8cde0 0%,#d3c7ac 40%,#5b5d63 100%)}
.years-row{display:flex;justify-content:center;align-items:center;margin-top:47px;font-family:"Roboto Condensed",sans-serif;font-weight:700;letter-spacing:-2px}
.years-words{font-size:33px;line-height:30px;text-align:right;margin-right:4px}
.years-num{font-size:74px;line-height:62px;letter-spacing:-5px}
.years-sub{font-family:"Roboto Condensed",sans-serif;font-weight:300;font-size:20px;line-height:21px;margin-top:4px}
.licensed{left:0;top:326px;background:linear-gradient(180deg,#3a4570,#2b3562);color:var(--white);text-align:center}
.licensed h2{font-size:17px;font-weight:700;line-height:23.5px;margin-top:55px}
.licensed .rule{width:212px;height:3px;background:var(--orange);margin:7px auto 8px}
.licensed .lic{font-size:9.5px;line-height:12px;color:var(--orange)}
.clients{left:286px;top:326px;width:285px;background:var(--slate);color:var(--white)}
.section-title{display:flex;align-items:center;font-family:"Archivo",sans-serif;font-weight:800;font-size:14px;letter-spacing:1px}
.section-title::after{content:"";flex:1;height:3px;background:var(--orange);margin-left:6px}
.clients .section-title{margin:22px 0 0 33px}
.clients .intro{font-size:9.5px;line-height:11px;margin:2px 0 0 35px}
.client-grid{display:grid;grid-template-columns:1fr 1fr;gap:14px 6px;margin:18px 14px 0 24px}
.client{display:flex;align-items:center;justify-content:center;gap:5px;height:46px;font-size:14px;font-weight:700;color:#a9aaad}
.client .dot{width:10px;height:10px;border-radius:50%;background:#a9aaad}
.services{left:571px;top:326px;background:linear-gradient(180deg,#303b66,#2b3562);color:var(--white)}
.services .section-title{margin:24px 0 0 34px}
.services ul{list-style:none;margin:10px 0 0 39px}
.services li{display:flex;align-items:flex-start;font-size:18px;line-height:20px;margin-bottom:0.5px}
.services li svg{flex:none;margin:3px 3px 0 0}
.footer{position:absolute;left:0;top:531px;width:857px;height:81px;background:var(--orange)}
.cta{position:absolute;right:527px;top:12px;width:300px;text-align:right;font-size:15.5px;line-height:18.5px;color:var(--dark);white-space:nowrap}
.cta b{font-weight:700}
.divider{position:absolute;top:13px;width:4px;height:56px;background:var(--dark)}
.pin{position:absolute;left:355px;top:24px}
.address{position:absolute;left:377px;top:25px;font-size:11.5px;line-height:14px;color:var(--white);white-space:nowrap}
.contacts{position:absolute;left:520px;top:21px;font-size:11px;line-height:17px;color:var(--white);white-space:nowrap}
.contacts div{display:flex;align-items:center;gap:3px}
.social{position:absolute;left:722px;top:22px;color:var(--white)}
.social p{font-size:8.5px;margin-bottom:6px}
.social .icons{display:flex;gap:5px}
.social .icons span{width:17px;height:17px;border-radius:50%;background:var(--dark)}
</style>
</head>
<body>
<main class="ad">
  <header class="header">
    <h1 class="headline">Delivering Safe, Timely<br>&amp; Quality Workmanship</h1>
    <div class="brand">
      <div class="brand-mark"></div>
      <div class="brand-name"><span class="n1">Marrowcrest</span><span class="n2">Construction, Inc.</span></div>
    </div>
  </header>

  <div class="cell photo-store" role="img" aria-label="Photo of a newly built retail storefront with crew on a lift"></div>
  <section class="cell years">
    <div class="years-row">
      <div class="years-words">OVER<br>YEARS</div>
      <div class="years-num">100</div>
    </div>
    <p class="years-sub">Collective commercial<br>experience</p>
  </section>
  <div class="cell photo-lot" role="img" aria-label="Aerial photo of a completed commercial building and parking lot"></div>

  <section class="cell licensed">
    <h2>We are Licensed<br>Contractors in California,<br>Oregon, and Washington</h2>
    <div class="rule"></div>
    <p class="lic">CA License No. 000000, OR License No. 000001<br>WA License No. MARROWC000X1</p>
  </section>

  <section class="cell clients">
    <h2 class="section-title">CLIENTS</h2>
    <p class="intro">Some of our repeat clients who trust us to<br>complete their commercial building projects</p>
    <div class="client-grid">
      <div class="client"><span class="dot"></span>Fieldline Sports</div>
      <div class="client">Brickoven Pies</div>
      <div class="client">Hearthmill Bakery</div>
      <div class="client">Pantry &amp; Co.</div>
    </div>
  </section>

  <section class="cell services">
    <h2 class="section-title">OUR SERVICES</h2>
    <ul>
      <li><svg width="12" height="12" viewBox="0 0 12 12"><rect x="1" y="2" width="9" height="9" fill="none" stroke="#fff" stroke-width="1.4"/><path d="M3 6l2 2 6-7" fill="none" stroke="#fff" stroke-width="1.6"/></svg>Commercial New<br>Construction</li>
      <li><svg width="12" height="12" viewBox="0 0 12 12"><rect x="1" y="2" width="9" height="9" fill="none" stroke="#fff" stroke-width="1.4"/><path d="M3 6l2 2 6-7" fill="none" stroke="#fff" stroke-width="1.6"/></svg>Strip Mall Renovation</li>
      <li><svg width="12" height="12" viewBox="0 0 12 12"><rect x="1" y="2" width="9" height="9" fill="none" stroke="#fff" stroke-width="1.4"/><path d="M3 6l2 2 6-7" fill="none" stroke="#fff" stroke-width="1.6"/></svg>Office Park Builder</li>
      <li><svg width="12" height="12" viewBox="0 0 12 12"><rect x="1" y="2" width="9" height="9" fill="none" stroke="#fff" stroke-width="1.4"/><path d="M3 6l2 2 6-7" fill="none" stroke="#fff" stroke-width="1.6"/></svg>Tilt-Up Construction</li>
      <li><svg width="12" height="12" viewBox="0 0 12 12"><rect x="1" y="2" width="9" height="9" fill="none" stroke="#fff" stroke-width="1.4"/><path d="M3 6l2 2 6-7" fill="none" stroke="#fff" stroke-width="1.6"/></svg>Construction Consulting &amp;<br>Planning</li>
    </ul>
  </section>

  <footer class="footer">
    <p class="cta">Contact us to learn how we can help<br>you develop your new <b>commercial<br>building or renovation project</b></p>
    <div class="divider" style="left:342px"></div>
    <svg class="pin" width="15" height="21" viewBox="0 0 15 21"><path d="M7.5 0C3.4 0 0 3.3 0 7.4 0 12.6 7.5 21 7.5 21S15 12.6 15 7.4C15 3.3 11.6 0 7.5 0z" fill="#1f2440"/><circle cx="7.5" cy="7.4" r="2.8" fill="#cc7c00"/></svg>
    <p class="address">2760 Alder Ridge #4<br>Sacramento, CA 95811<br>United States</p>
    <div class="contacts">
      <div><svg width="12" height="12" viewBox="0 0 12 12"><path d="M2.5 1l2 2.2-1 1.4a7 7 0 003.9 3.9l1.4-1L11 9.5 9.6 11C5 11 1 7 1 2.4z" fill="#1f2440"/></svg>(555) 014-2273</div>
      <div><svg width="12" height="10" viewBox="0 0 12 10"><rect x=".5" y="1" width="11" height="8" fill="#1f2440"/><path d="M1 1.5l5 4 5-4" fill="none" stroke="#cc7c00"/></svg>info@marrowcrestbuilding.com</div>
      <div><svg width="12" height="12" viewBox="0 0 12 12"><circle cx="6" cy="6" r="5" fill="none" stroke="#1f2440" stroke-width="1.3"/><path d="M1 6h10M6 1c-2.5 3-2.5 7 0 10M6 1c2.5 3 2.5 7 0 10" fill="none" stroke="#1f2440"/></svg>www.marrowcrestbuilding.com</div>
    </div>
    <div class="divider" style="left:713px"></div>
    <div class="social">
      <p>Follow us on social media</p>
      <div class="icons"><span></span><span></span><span></span></div>
    </div>
  </footer>
</main>
</body>
</html>
```